Help Design the Packaging for our Nicotine Replacement Therapy

Packaging Design Brief for Brevora
We are using this contest to find a designer who can design the packaging for the full line of products listed below for our new brand. This contest will require you to provide designs for the Traditional mint in both the 2mg and 4mg, and the Traditional Cinnamon 2 mg and 4mg, plus the mint in the Modern, 2mg and 4mg. We would like to see how you propose to tie the designs together so their is clear differentiate between the products and flavors, yet it maintains brand cohesiveness.
We would like to then work with the contest winner on a 1-1 project to develop the packaging for the remaining products.
Project Overview:
Brevora is launching a new line of nicotine replacement therapy (NRT) products, including gum and lozenges in multiple flavors and strengths. The packaging design needs to reflect Brevora’s brand values of trust, warmth, professionalism, and customer-centricity while being visually appealing, functional, and easily distinguishable.
Here is our full product line up so you can design product packaging that has the potential to expand as we add more flavors.
Product Line-Up:
1. Nicotine Gum ("Traditional" because it tastes and feels like hollbeck's gum):
- Flavors: Mint, Fruit, Cinnamon
- Strengths: 2mg, 4mg
- Pack Size: 240 pieces per pack
2. Nicotine Gum (Stiffer, Playdough-Like Texture will be called "Classic"):
- Strengths: 2mg, 4mg
3. Nicotine Lozenges:
- Flavors: Mint, Citrus, Berry
- Strengths: 2mg, 4mg
- Pack Size: 120 pieces per pack
Design Objectives:
1. Brand Consistency:
- The Brevora logo should be easily recognizable across all packaging.
- The design should reflect the brand’s personality: trustworthy, professional, warm, and approachable.
- Packaging should evoke a sense of reliability and comfort, appealing to a mature audience.
2. Differentiation:
- Flavor Differentiation:
- Use distinct colors for each flavor to ensure they are easily distinguishable.
- Incorporate icons or images that represent the flavor (e.g., mint leaves for Mint, cinnamon sticks for Cinnamon).
- Strength Differentiation:
- Clearly display the nicotine strength (2mg or 4mg) in a way that stands out at a glance.
- Gum Texture Differentiation:
- Create a visual distinction between the traditional chewing gum and the stiffer, playdough-like gum while maintaining a cohesive brand look.
- Consider using different background textures, patterns, or additional design elements to indicate the different textures while ensuring they still feel part of the same family.
3. Product Type Differentiation:
- Gum vs. Lozenges:
- The lozenges should be visually distinct from the gum products while still fitting within the overall Brevora brand aesthetic.
- Consider using a different shape or design element on the lozenge packaging (e.g., a lozenge icon or a unique pattern) to differentiate them from the gum.
- Maintain consistent use of colors for flavors across both gum and lozenge packaging (e.g., Mint gum and Mint lozenges should share the same color scheme) to unify the product line.
4. Scalability:
- The design should be flexible enough to accommodate additional flavors or product variations in the future.
- Ensure that any new flavor or product type can be easily integrated into the existing design template.
Content Requirements:
1. Front of Pack:
- Brevora logo
- Flavor name and representative image
- Nicotine strength (2mg or 4mg)
- Indication of gum type (Traditional or Stiffer texture)
- Pack size (e.g., "240 Pieces")
2. Here are the die lines from the manufacturer. You will see that there are certain things that must be included on the gum packaging:
https://files.tarnowbox.net/folders/8qpe27Lm_X4v81ZsKd0n-WRyTa3GbU7Hc?usp=share_link
Overall Feel:
- The packaging should communicate that Brevora is a trustworthy, professional brand with a warm, supportive approach. It should feel modern and appeal to a broad audience both male and female.
Packaging design for all SKUs listed above, with clear differentiation between flavors, strengths, and product types.
Here is the link to the brevora logo. https://files.tarnowbox.net/file/d/7-RHbwPqJmm412LcuvzxAq3QWEtn5ZK9S/view?usp=sharing We are not opposed to the color of the dots and + sign changing to signify flavor either.
Target Market(s)
individuals 18-55+ looking to quit vaping and smoking
Industry/Entity Type
nicotine replacement therapy
Other font styles liked:
- should compliment and look good with our logo and font which is Nexa bold
Requirements
Must have
- we want to look professional and trustworthy. . .and we want a design that is cohesive across the product set and can expand and stay on brand with additional flavors.
Nice to have
- We will pick a winner and then pay that winner to do the rest of the package designs for each sku and lozenges too.

```html
<!DOCTYPE html>
<html lang="en">
<head>
<meta charset="utf-8">
<title>Brevora Lozenge Packaging</title>
<link href="https://fonts.googleapis.com/css2?family=Outfit:wght@300;400;600;700&family=Bodoni+Moda:wght@400;500&display=swap" rel="stylesheet">
<style>
  :root {
    --stage: #dfe9e6;
    --dark: #2a1f28;
    --mint: #1c9c8a;
    --mint-bright: #1ea592;
    --mint-soft: #93d9c9;
    --gold: #cfa43a;
    --gold-line: #d9b23a;
    --gold-num: #d6aa26;
    --paper: #ececec;
    --leaf-a: #3fae4a;
    --leaf-b: #1f6e2a;
    --fruit-a: #9a6fc4;
    --fruit-b: #e8c23a;
  }
  * { margin: 0; padding: 0; box-sizing: border-box; }
  html, body { width: 1200px; height: 960px; overflow: hidden; background: var(--stage); }
  .canvas { position: relative; width: 1200px; height: 960px; }

  .pack { position: absolute; overflow: hidden; }
  .pack-shape { position: absolute; inset: 0; }

  /* Mint lozenge front */
  .pack--mint { left: 588px; top: 171px; width: 352px; height: 498px; background: var(--mint); }
  .brand { position: absolute; left: 30px; top: 30px; display: flex; align-items: center; gap: 7px;
    font-family: "Outfit", sans-serif; font-weight: 700; font-size: 38px; color: var(--paper); letter-spacing: -0.4px; line-height: 1; }
  .brand-dot { width: 10px; height: 10px; border-radius: 50%; background: #3dbb4a; }
  .strength { position: absolute; left: 258px; top: 26px; width: 64px; text-align: center; font-family: "Outfit", sans-serif; color: var(--gold-num); line-height: 1; }
  .strength-num { font-size: 74px; font-weight: 700; display: block; line-height: 0.9; }
  .strength-unit { font-size: 16px; font-weight: 400; display: block; margin-top: 0; }
  .active { position: absolute; left: 30px; top: 100px; font-family: "Outfit", sans-serif; font-weight: 600; font-size: 15px; color: var(--paper); line-height: 1.2; }
  .product-type { position: absolute; left: 29px; top: 122px; font-family: "Outfit", sans-serif; font-weight: 700; font-size: 34px; color: var(--mint-bright); letter-spacing: 0.4px; line-height: 1.1; }
  .flavor-art { position: absolute; border-radius: 42% 46% 40% 48%; }
  .flavor-art--mint { left: 72px; top: 184px; width: 249px; height: 168px; background: radial-gradient(ellipse at 45% 42%, var(--leaf-a), var(--leaf-b) 68%, transparent 71%); }
  .pack--mint .flavor { position: absolute; left: 112px; top: 364px; width: 224px; text-align: center; }
  .flavor-name { font-family: "Bodoni Moda", serif; font-weight: 400; font-size: 35px; color: var(--paper); line-height: 1.1; white-space: nowrap; }
  .flavor-note { font-family: "Outfit", sans-serif; font-size: 12.5px; color: var(--paper); margin-top: 2px; white-space: nowrap; }
  .pack--mint .count { position: absolute; left: 29px; top: 388px; font-family: "Outfit", sans-serif; color: var(--paper); line-height: 1; }
  .count-num { font-size: 17px; font-weight: 700; display: block; }
  .count-unit { font-size: 9px; font-weight: 600; display: block; margin-top: 3px; letter-spacing: 0.3px; }
  .pack--mint .tagline { position: absolute; left: 0; right: 0; top: 444px; text-align: center; font-family: "Outfit", sans-serif; font-weight: 300; font-size: 23px; color: var(--mint-soft); line-height: 1.2; }

  /* Fruit front, set sideways */
  .pack--fruit { left: 261px; top: 291px; width: 329px; height: 378px; background: var(--gold); }
  .pack-rotated { position: absolute; left: 329px; top: 0; width: 378px; height: 329px; transform-origin: 0 0; transform: rotate(90deg); }
  .flavor-art--fruit { left: 109px; top: 56px; width: 196px; height: 124px; background: radial-gradient(ellipse at 45% 50%, var(--fruit-a), #d9503a 45%, var(--fruit-b) 64%, transparent 70%); }
  .pack--fruit .count { position: absolute; left: 40px; top: 226px; font-family: "Outfit", sans-serif; color: var(--dark); line-height: 1; }
  .pack--fruit .flavor { position: absolute; right: 42px; top: 202px; text-align: right; }
  .pack--fruit .flavor-name { color: var(--dark); font-size: 38px; line-height: 1; }
  .pack--fruit .flavor-note { color: var(--dark); font-size: 10.5px; margin-top: 4px; }
  .pack--fruit .tagline { position: absolute; left: 78px; top: 282px; font-family: "Outfit", sans-serif; font-weight: 300; font-size: 22px; color: var(--paper); line-height: 1.2; white-space: nowrap; }
</style>
</head>
<body>
<main class="canvas">

  <section class="pack pack--fruit" aria-label="Fruit lozenge pack front">
    <div class="pack-rotated">
      <svg class="pack-shape" viewBox="0 0 378 329" width="378" height="329" aria-hidden="true">
        <polygon points="0,0 249,0 0,201" fill="var(--dark)"/>
        <line x1="0" y1="201" x2="249" y2="0" stroke="var(--gold-line)" stroke-width="2"/>
        <circle cx="172" cy="90" r="88" fill="var(--dark)"/>
      </svg>
      <div class="flavor-art flavor-art--fruit" role="img" aria-label="Illustration of grapes, apple, kiwi, banana and orange with white lozenges"></div>
      <div class="count"><span class="count-num">240</span><span class="count-unit">PIECES</span></div>
      <div class="flavor">
        <div class="flavor-name">FRUIT</div>
        <div class="flavor-note">COATED FOR EXTREME FLAVOR</div>
      </div>
      <div class="tagline">Long-Lasting Flavor</div>
    </div>
  </section>

  <section class="pack pack--mint" aria-label="Cool Mint lozenge pack front">
    <svg class="pack-shape" viewBox="0 0 352 498" width="352" height="498" aria-hidden="true">
      <polygon points="0,0 352,0 352,78 0,359" fill="var(--dark)"/>
      <line x1="0" y1="359" x2="352" y2="78" stroke="var(--gold-line)" stroke-width="2"/>
      <circle cx="165" cy="270" r="86" fill="var(--dark)"/>
    </svg>
    <div class="brand"><span>Brevora</span><span class="brand-dot"></span></div>
    <div class="strength"><span class="strength-num">4</span><span class="strength-unit">mg</span></div>
    <div class="active">Nicotine Polacrilex</div>
    <div class="product-type">LOZENGE</div>
    <div class="flavor-art flavor-art--mint" role="img" aria-label="Illustration of mint leaves with two white speckled lozenges"></div>
    <div class="count"><span class="count-num">240</span><span class="count-unit">PIECES</span></div>
    <div class="flavor">
      <div class="flavor-name">COOL MINT</div>
      <div class="flavor-note">COATED FOR EXTREME FLAVOR</div>
    </div>
    <div class="tagline">Long-Lasting Flavor</div>
  </section>

</main>
</body>
</html>
```